Letterhead Design

We need a new Letterhead design for a 30 year old Electrical Company. We service domestic and commercial places. We have a logo recently made so to incorporate that. Using same colours or interested to see others added.
Would like to see a couple of options with all the info in letterhead, then another with info in a footnote down the bottom.

info needed to be added:

-Lic. No 48120
3/22-24 Tallow Rd, Kelsford 2207
W - dorrickpower.com.au
T - (02) 9483 1720
M - 0437 592 816
E - info@dorrickpower.com.au
ABN: 41 729 504 316

```html
<!DOCTYPE html>
<html lang="en">
<head>
<meta charset="utf-8">
<title>Dorrick Power Letterhead</title>
<link href="https://fonts.googleapis.com/css2?family=Questrial&family=Montserrat:wght@600;700&display=swap" rel="stylesheet">
<style>
  :root {
    --backdrop: #1d4847;
    --teal: #124542;
    --orange: #f09a1e;
    --paper: #ffffff;
    --ink: #2b2b2b;
    --body-ink: #4a4a4a;
    --faint: #e4e6e6;
  }
  * { box-sizing: border-box; margin: 0; padding: 0; }
  html, body {
    width: 1200px; height: 1200px; overflow: hidden;
    background: var(--backdrop);
  }
  .sheet {
    position: absolute; left: 211px; top: 50px;
    width: 778px; height: 1100px;
    background: var(--paper);
    overflow: hidden;
    font-family: "Questrial", sans-serif;
    color: var(--body-ink);
  }
  .edge { position: absolute; left: 0; width: 100%; height: 60px; }
  .edge--top { top: 0; }
  .edge--bottom { bottom: 0; }

  .brand {
    position: absolute; left: 60px; top: 62px;
    font-family: "Questrial", sans-serif;
    font-size: 40px; color: var(--teal);
    letter-spacing: 0.5px;
    display: flex; align-items: center; gap: 12px;
  }
  .brand__mark { width: 14px; height: 14px; background: var(--orange); }
  .brand__rule {
    position: absolute; left: 60px; top: 112px; width: 260px; height: 2px;
    background: var(--orange);
  }
  .brand__est {
    position: absolute; left: 248px; top: 116px;
    font-family: "Montserrat", sans-serif; font-weight: 600;
    font-size: 14px; color: var(--teal);
  }

  .contact {
    position: absolute; right: 50px; top: 140px;
    padding-left: 16px; border-left: 2px solid var(--orange);
    font-family: "Montserrat", sans-serif; font-weight: 600;
    font-size: 10.5px; line-height: 1.55; color: var(--teal);
    list-style: none;
  }
  .contact li { display: flex; gap: 6px; align-items: flex-start; }
  .contact svg { width: 10px; height: 10px; margin-top: 3px; flex: none; }
  .contact .gap { margin-top: 10px; }
  .contact .web { font-weight: 700; font-size: 12px; }

  .letter {
    position: absolute; left: 60px; top: 290px; width: 650px;
    font-size: 12.5px; line-height: 1.55;
  }
  .letter__greeting {
    font-family: "Montserrat", sans-serif; font-weight: 700;
    color: var(--ink); font-size: 14px; margin-bottom: 14px;
  }
  .letter p { margin-bottom: 14px; }

  .signature {
    position: absolute; left: 400px; top: 800px; width: 260px; height: 70px;
    background: var(--faint); opacity: .6;
  }
  .watermark {
    position: absolute; left: 170px; top: 885px;
    font-family: "Questrial", sans-serif;
    font-size: 120px; color: var(--faint);
    letter-spacing: -2px;
  }
</style>
</head>
<body>
  <main class="sheet">
    <svg class="edge edge--top" viewBox="0 0 778 60" preserveAspectRatio="none">
      <path d="M0 0 H320 V6 H0 Z" fill="#124542"/>
      <path d="M320 0 Q560 6 778 40 V46 Q560 12 320 6 Z" fill="#f09a1e"/>
    </svg>

    <header>
      <div class="brand"><span class="brand__mark"></span>Dorrick Power</div>
      <div class="brand__rule"></div>
      <div class="brand__est">Est. 1980</div>

      <ul class="contact">
        <li><svg viewBox="0 0 10 10"><path d="M5 0 L10 5 H8.5 V10 H1.5 V5 H0 Z" fill="#f09a1e"/></svg><span>3/22-24 Tallow Rd,<br>Kelsford 2207</span></li>
        <li class="gap"><svg viewBox="0 0 10 10"><rect x="0.5" y="2" width="9" height="6" fill="none" stroke="#f09a1e"/></svg><span>ABN: 41 729 504 316</span></li>
        <li class="gap"><svg viewBox="0 0 10 10"><path d="M1 1 L4 1 L4.5 3.5 L3 4.5 Q4.5 7 5.5 7 L6.5 5.5 L9 6 V9 Q1 9 1 1Z" fill="#f09a1e"/></svg><span>(02) 9483 1720</span></li>
        <li><svg viewBox="0 0 10 10"><rect x="2.5" y="0.5" width="5" height="9" rx="1" fill="none" stroke="#f09a1e"/></svg><span>0437 592 816</span></li>
        <li><svg viewBox="0 0 10 10"><rect x="0.5" y="2" width="9" height="6" fill="none" stroke="#f09a1e"/><path d="M0.5 2 L5 5.5 L9.5 2" fill="none" stroke="#f09a1e"/></svg><span>info@dorrickpower.com.au</span></li>
        <li class="web"><svg viewBox="0 0 10 10"><circle cx="5" cy="5" r="4.5" fill="#f09a1e"/></svg><span>dorrickpower.com.au</span></li>
      </ul>
    </header>

    <article class="letter">
      <p class="letter__greeting">Lorem ipsum dolor sit amet,</p>
      <p>Lorem ipsum dolor sit amet, consectetuer adipiscing elit. Aenean commodo ligula eget dolor. Aenean massa. Cum sociis natoque penatibus et magnis dis parturient montes, nascetur ridiculus mus. Donec quam felis, ultricies nec, pellentesque eu, pretium quis, sem. Nulla consequat massa quis enim. Donec pede justo, fringilla vel, aliquet nec, vulputate eget, arcu.</p>
      <p>In enim justo, rhoncus ut, imperdiet a, venenatis vitae, justo. Nullam dictum felis eu pede mollis pretium. Integer tincidunt. Cras dapibus. Vivamus elementum semper nisi. Aenean vulputate eleifend tellus. Aenean leo ligula, porttitor eu, consequat vitae, eleifend ac, enim. Aliquam lorem ante, dapibus in, viverra quis, feugiat a, tellus.</p>
      <p>Phasellus viverra nulla ut metus varius laoreet. Quisque rutrum. Aenean imperdiet. Etiam ultricies nisi vel augue. Curabitur ullamcorper ultricies nisi. Nam eget dui. Etiam rhoncus. Maecenas tempus, tellus eget condimentum rhoncus, sem quam semper libero, sit amet adipiscing sem neque sed ipsum. Nam quam nunc, blandit vel, luctus pulvinar, hendrerit id, lorem. Maecenas nec odio et ante tincidunt tempus. Donec vitae sapien ut libero venenatis faucibus. Nullam quis ante. Etiam sit amet orci eget eros faucibus tincidunt. Duis leo. Sed fringilla mauris sit amet nibh.</p>
      <p>Donec sodales sagittis magna. Sed consequat, leo eget bibendum sodales, augue velit cursus nunc. In enim justo, rhoncus ut, imperdiet a, venenatis vitae, justo. Nullam dictum felis eu pede mollis pretium. Integer tincidunt. Cras dapibus. Vivamus elementum semper nisi. Aenean vulputate eleifend tellus. Aenean leo ligula, porttitor eu, consequat vitae, eleifend ac, enim. Aliquam lorem ante, dapibus in, viverra quis, feugiat a, tellus.</p>
    </article>

    <div class="signature" role="img" aria-label="Handwritten signature of the sender"></div>
    <div class="watermark" aria-hidden="true">Dorrick</div>

    <svg class="edge edge--bottom" viewBox="0 0 778 60" preserveAspectRatio="none">
      <path d="M0 14 Q220 50 480 54 V60 Q220 56 0 20 Z" fill="#f09a1e"/>
      <path d="M480 54 H778 V60 H480 Z" fill="#124542"/>
    </svg>
  </main>
</body>
</html>
```